Business Card Design Project

I am community manager and social media strategist. I need a double sided business card with company logo and name. Looking for something professional, elegant but also a little bit original.

Industry/Entity Type

Business

Requirements
Must have
• - The logo and the colours are the company colours and a required to stay.
- The size should be: 84 x 55 mm (or 3.30 x 2.16)
- The file size should be: 1039 x 697 pixels (300 dpi)
- I'd like rounded corners. :)

Use the following contact information for the card:

Lucile Bravant
Stratégie médias sociaux / community management / édition de sites sociaux
mob. : 0687152930
lucile.bravant@maivox.fr
Twitter. : @lbravant
Skype : bravant.lucile

```html
<!DOCTYPE html>
<html lang="fr">
<head>
<meta charset="utf-8">
<title>Carte de visite – Lucile Bravant</title>
<link rel="stylesheet" href="https://fonts.googleapis.com/css2?family=Open+Sans:wght@400;700&family=Arimo:wght@400&display=swap">
<style>
  :root {
    --page: #ffffff;
    --card-cream: #f0f2dc;
    --card-navy: #065a87;
    --navy-deep: #043f60;
    --brand-blue: #1f6aa5;
    --ink: #1c1c1c;
    --wave-blue: #4f8fc0;
    --wave-sky: #8cc2dc;
    --wave-mist: #d9ddd2;
    --shadow: rgba(0, 0, 0, 0.55);
  }
  * { margin: 0; padding: 0; box-sizing: border-box; }
  html, body {
    width: 1200px; height: 568px; overflow: hidden;
    background: var(--page);
  }
  .canvas { position: relative; width: 1200px; height: 568px; }
  .card {
    position: absolute; top: 103px;
    width: 517px; height: 340px;
    border-radius: 36px; overflow: hidden;
    box-shadow: 12px 12px 14px var(--shadow);
  }
  .card--front { left: 55px; background: var(--card-cream); }
  .card--back { left: 615px; background: var(--card-navy); }
  .card svg.waves { position: absolute; inset: 0; }

  .brand {
    position: absolute; left: 40px; top: 40px;
    display: flex; flex-direction: column; align-items: flex-start; gap: 8px;
  }
  .brand__dot {
    width: 72px; height: 72px; border-radius: 50%;
    background: var(--brand-blue); margin-left: 22px;
  }
  .brand__name {
    font-family: "Open Sans", sans-serif; font-weight: 700;
    font-size: 30px; letter-spacing: 1px; color: var(--brand-blue); line-height: 1;
  }

  .holder {
    position: absolute; right: 20px; top: 76px; width: 260px;
    font-family: "Arimo", sans-serif; color: var(--ink);
  }
  .holder__name {
    font-family: "Open Sans", sans-serif; font-size: 19px;
    position: absolute; left: 35px; top: 0; white-space: nowrap;
  }
  .holder__role { position: absolute; top: 32px; left: 0; font-size: 13px; line-height: 26.5px; white-space: nowrap; }
  .holder__role span { display: block; }
  .holder__role span + span { padding-left: 44px; }

  .contact {
    position: absolute; left: 47px; top: 217px;
    font-family: "Arimo", sans-serif; font-size: 14.5px; color: var(--ink);
    list-style: none; line-height: 29px;
  }
  .contact .phone { letter-spacing: 1.6px; }

  .back-mark {
    position: absolute; left: 120px; top: -70px;
    width: 310px; height: 310px; border-radius: 50%;
    background: var(--navy-deep); opacity: 0.55;
  }
</style>
</head>
<body>
<main class="canvas">
  <section class="card card--front" aria-label="Recto">
    <svg class="waves" width="517" height="340" viewBox="0 0 517 340" aria-hidden="true">
      <path d="M0 150 C140 140 330 170 517 222 L517 240 C330 190 150 165 0 172 Z" fill="var(--wave-mist)" opacity="0.9"/>
      <path d="M0 180 C150 168 320 195 517 250 L517 262 C320 212 150 186 0 194 Z" fill="var(--wave-blue)" opacity="0.75"/>
      <path d="M0 192 C170 182 340 212 517 268 L517 276 C340 224 170 196 0 204 Z" fill="var(--wave-sky)" opacity="0.8"/>
      <path d="M0 160 C170 150 340 185 517 232 L517 238 C340 192 170 158 0 166 Z" fill="var(--wave-sky)" opacity="0.6"/>
    </svg>
    <div class="brand">
      <span class="brand__dot" aria-hidden="true"></span>
      <span class="brand__name">ALIZENA</span>
    </div>
    <div class="holder">
      <h1 class="holder__name">Lucile Bravant</h1>
      <p class="holder__role">
        <span>Stratégie médias sociaux /</span>
        <span>community management /</span>
        <span>édition de sites sociaux</span>
      </p>
    </div>
    <ul class="contact">
      <li>mobile. : <span class="phone">0687152930</span></li>
      <li>lucile.bravant@maivox.fr</li>
      <li>Twitter. : @lbravant</li>
      <li>Skype : bravant.lucile</li>
    </ul>
  </section>

  <section class="card card--back" aria-label="Verso">
    <span class="back-mark" aria-hidden="true"></span>
    <svg class="waves" width="517" height="340" viewBox="0 0 517 340" aria-hidden="true">
      <path d="M0 240 C170 245 340 275 517 330 L517 340 C340 288 170 258 0 254 Z" fill="#4f86b3" opacity="0.7"/>
      <path d="M0 262 C180 262 350 290 517 340 L500 340 C340 298 180 276 0 276 Z" fill="#9cc0d8" opacity="0.6"/>
      <path d="M300 300 C390 310 460 320 517 300 L517 318 C460 336 400 330 340 318 Z" fill="#2a8ccc" opacity="0.6"/>
    </svg>
  </section>
</main>
</body>
</html>
```